missions focus sunday

i am a christian who is tasked to do a simple presentation of missions work in northern germany. i have some ideas which i have sketched out as enclosed.
can you do the postcard in black background with words/diagrams in white? thanks

```html
<!DOCTYPE html>
<html lang="en">
<head>
<meta charset="utf-8">
<title>Missions Focus Sunday – Postcard</title>
<link rel="stylesheet" href="https://fonts.googleapis.com/css2?family=Dancing+Script:wght@500;700&display=swap">
<style>
  :root {
    --card-black: #000000;
    --ink-white: #ffffff;
    --cloud-white: #f4f4f4;
    --cloud-edge: #bdbdbd;
    --cloud-text: #111111;
    --flag-dark: #1a1a1a;
    --flag-mid: #7a7a7a;
    --flag-light: #c9c9c9;
    --flag-grey: #9a9a9a;
    --emblem-fill: #d0d0d0;
    --dot-line: #cfcfcf;
    --skyline-top: rgba(60, 60, 60, 0);
    --skyline-bottom: #4a4a4a;
  }
  html, body {
    margin: 0;
    padding: 0;
    width: 1200px;
    height: 922px;
    overflow: hidden;
    background: var(--card-black);
  }
  .postcard {
    position: relative;
    width: 1200px;
    height: 922px;
    background: var(--card-black);
    font-family: "Dancing Script", cursive;
    color: var(--ink-white);
  }
  .postcard-art {
    position: absolute;
    inset: 0;
    width: 1200px;
    height: 922px;
    display: block;
  }
  .script-note {
    position: absolute;
    margin: 0;
    font-weight: 500;
    font-size: 34px;
    line-height: 1.2;
    color: var(--ink-white);
    white-space: nowrap;
  }
  .note-power { left: 70px; top: 170px; transform: rotate(-10deg); }
  .note-power .line-two { display: block; padding-left: 95px; }
  .note-call { left: 905px; top: 705px; transform: rotate(-8deg); }
  .note-call .line-one { display: block; padding-left: 70px; }
  .dream-line {
    position: absolute;
    left: 383px;
    width: 415px;
    top: 405px;
    margin: 0;
    text-align: center;
    font-weight: 500;
    font-size: 40px;
    line-height: 1.3;
    color: var(--cloud-text);
    transform: rotate(-3deg);
  }
</style>
</head>
<body>
<main class="postcard">
  <svg class="postcard-art" viewBox="0 0 1200 922" xmlns="http://www.w3.org/2000/svg">
    <defs>
      <linearGradient id="skyline-fade" x1="0" y1="0" x2="0" y2="1">
        <stop offset="0" stop-color="var(--skyline-top)"/>
        <stop offset="1" stop-color="var(--skyline-bottom)"/>
      </linearGradient>
      <marker id="arrow-head" viewBox="0 0 10 10" refX="5" refY="5" markerWidth="9" markerHeight="9" orient="auto">
        <path d="M0,0 L10,5 L0,10 Z" fill="var(--dot-line)"/>
      </marker>
    </defs>

    <rect class="skyline" x="0" y="745" width="1200" height="177" fill="url(#skyline-fade)"
          role="img" aria-label="Night city skyline silhouette with lit windows"/>

    <path class="journey-path" d="M150,560 C175,330 400,140 775,131"
          fill="none" stroke="var(--dot-line)" stroke-width="3" stroke-dasharray="2 8" stroke-linecap="round"
          marker-end="url(#arrow-head)"/>
    <path class="journey-path" d="M985,250 C1000,560 830,775 380,783"
          fill="none" stroke="var(--dot-line)" stroke-width="3" stroke-dasharray="2 8" stroke-linecap="round"
          marker-end="url(#arrow-head)"/>

    <rect class="footprints" x="225" y="245" width="145" height="80" rx="30" fill="#d8d8d8"
          role="img" aria-label="Two small white footprints"/>

    <g class="flag flag-germany">
      <rect x="844" y="111" width="194" height="39" fill="var(--flag-dark)"/>
      <rect x="844" y="150" width="194" height="39" fill="var(--flag-mid)"/>
      <rect x="844" y="189" width="194" height="39" fill="var(--flag-light)"/>
      <rect class="flag-emblem" x="914" y="116" width="54" height="106" rx="6" fill="#3a3a3a"
            role="img" aria-label="Eagle coat of arms emblem"/>
    </g>

    <g class="flag flag-singapore">
      <rect x="96" y="651" width="232" height="72" fill="var(--flag-grey)"/>
      <rect x="96" y="723" width="232" height="71" fill="var(--ink-white)"/>
      <rect class="flag-emblem" x="114" y="664" width="66" height="46" rx="8" fill="var(--emblem-fill)"
            role="img" aria-label="Crescent and stars flag emblem"/>
      <rect class="flag-tower" x="205" y="657" width="34" height="137" fill="#2a2a2a"
            role="img" aria-label="Airport control tower silhouette"/>
    </g>

    <rect class="airplane" x="790" y="590" width="110" height="100" rx="40" fill="#e6e6e6"
          transform="rotate(-35 845 640)" role="img" aria-label="White airplane in flight"/>

    <path class="dream-cloud"
          d="M440,545 C385,545 370,490 410,470 C375,440 400,385 450,395 C460,350 530,335 560,370
             C590,330 680,335 690,380 C740,360 790,395 770,440 C815,460 800,535 745,530
             C725,560 665,560 640,540 C610,565 540,565 515,540 C495,555 460,555 440,545 Z"
          fill="var(--cloud-white)" stroke="var(--cloud-edge)" stroke-width="3"/>
  </svg>

  <p class="script-note note-power">the power<span class="line-two">of 2</span></p>
  <p class="dream-line">Last night I<br>dream of this</p>
  <p class="script-note note-call"><span class="line-one">answer</span>the “come” call</p>
</main>
</body>
</html>
```